Talvera Web site

Talvera is a trade name for Dresgan enterprises llc, would like Dresgan mentioned but not prominent.

Use current logo to base colors and look/feel of website. Modern trendy look.

Talvera Technical Services - "Irrevocably committed to your success"

Website design for a nation wide service based company

Networking, AV, access control, automation, EAS, project management, consulting, electrical, design, service staffing

Hostwick hosts our URL's

Questions-
Who owns the content once accepted.
How is the content delivered to build site
How do we adjust. or add to content once published

Target Market(s)

commercial and retail technical services. IE, we provide technical services for retail and commercial vertical markets

Industry/Entity Type

Trade

Coding

Coded - Design and coding required

Number of Pages Required

5+ page

Font styles to use
Sans Serif

Colors
3276b5

Requirements
Must have
• Pages-
• About/info, contact, services, customers log in portal, social media links
• links to outside web based software portals
• Call through (call me) links

```html
<!DOCTYPE html>
<html lang="en">
<head>
<meta charset="utf-8">
<title>Talvera Technical Services</title>
<link rel="stylesheet" href="https://fonts.googleapis.com/css2?family=Merriweather:wght@400;700&family=Open+Sans:wght@400;600;700&family=Tinos&display=swap">
<style>
:root{
  --brand:#3276b5;
  --ink:#111;
  --white:#fff;
  --dark:#1f1f1f;
  --footer:#2b2b2b;
  --footer-deep:#1c1c1c;
  --muted:#9a9a9a;
  --line:#e3e3e3;
  --client-grey:#bdbdbd;
  --client-red:#b0171f;
}
*{box-sizing:border-box;margin:0;padding:0}
html,body{width:1200px;height:2222px;overflow:hidden;background:var(--white)}
body{position:relative;font-family:"Open Sans",sans-serif;color:var(--ink)}
.abs{position:absolute}

/* header */
.site-header{position:absolute;left:0;top:0;width:1200px;height:84px;background:var(--white)}
.brand{position:absolute;left:104px;top:14px;display:flex;align-items:center;gap:12px}
.brand-dot{width:52px;height:52px;border-radius:50%;background:var(--brand)}
.brand-name{font-family:"Open Sans",sans-serif;font-weight:700;color:var(--brand);line-height:1}
.brand-name .main{display:block;font-size:33px;letter-spacing:0.5px}
.brand-name .sub{display:block;font-size:12px;letter-spacing:1.4px;margin-top:4px}
.nav a{position:absolute;top:0;height:74px;line-height:92px;font-size:14px;color:#555;text-decoration:none}
.nav .home{left:567px;width:80px;background:var(--brand);color:var(--white);font-weight:700;text-align:center;border-bottom:4px solid #245a8c;line-height:1}
.nav .home svg{display:block;margin:18px auto 8px}

/* hero */
.hero{position:absolute;left:0;top:84px;width:1200px;height:614px;background:linear-gradient(180deg,#7c8590 0%,#5b636e 45%,#3b4048 100%)}
.hero-title{position:absolute;left:0;width:1200px;text-align:center;font-family:"Merriweather",serif;color:var(--white);text-shadow:0 2px 4px rgba(0,0,0,.35)}
.hero-title .light{top:228px;font-size:46px;font-weight:400}
.hero-title .bold{top:284px;font-size:51px;font-weight:700}

/* section headings */
.section-title{position:absolute;left:0;width:1200px;text-align:center;font-family:"Merriweather",serif;font-size:31px;font-weight:400}
.divider{position:absolute}

.about-text{position:absolute;left:150px;top:838px;width:900px;text-align:center;font-family:"Tinos",serif;font-size:14.5px;line-height:22.5px;color:var(--ink)}

/* services */
.services{position:absolute;left:0;top:984px;width:1200px;height:429px;background:var(--dark)}
.service{position:absolute;top:200px;width:220px;text-align:center}
.service .disc{width:116px;height:116px;margin:0 auto;border-radius:50%;background:var(--white);display:flex;align-items:center;justify-content:center}
.service .label{margin-top:24px;font-family:"Merriweather",serif;font-size:16px;color:var(--white)}

/* clients */
.client-row{position:absolute;left:198px;top:1598px;width:808px;height:184px;border:1px solid var(--line);display:flex}
.client{flex:1;border-right:1px solid var(--line);display:flex;align-items:center;justify-content:center;font-family:"Merriweather",serif;font-weight:700;font-size:36px;color:var(--client-grey)}
.client:last-child{border-right:0}
.client.is-active{color:var(--client-red)}
.arrow{position:absolute;top:1675px}

/* footer */
.site-footer{position:absolute;left:0;top:1852px;width:1200px;height:311px;background:var(--footer)}
.footer-heading{position:absolute;font-size:17px;color:var(--white);font-weight:400;letter-spacing:.2px}
.event{position:absolute;left:110px;width:260px}
.event .date{position:absolute;left:0;top:0;width:38px;height:55px;background:#0d0d0d;color:var(--white);text-align:center}
.event .date b{display:block;font-size:21px;line-height:30px;margin-top:4px}
.event .date span{display:block;font-size:10px;line-height:12px}
.event p,.news p{font-size:13px;line-height:18px;color:var(--muted)}
.event p{margin-left:48px}
.news{position:absolute;left:437px;width:230px}
.news small{display:block;font-size:11px;color:var(--white);margin-top:1px}
.quick-links{position:absolute;left:721px;top:1922px;list-style:none}
.quick-links li{font-size:12px;line-height:18px;color:#bbb}
.social{position:absolute;left:720px;top:2070px;display:flex;gap:10px}
.social span{display:flex;align-items:center;gap:4px;font-size:11px;color:var(--white)}
.social i{display:block;width:16px;height:16px;border-radius:50%;background:var(--white)}
.connect{position:absolute;left:907px;top:1918px;width:210px;font-size:13px;line-height:20px;color:var(--muted)}
.connect dl{margin-top:8px;display:grid;grid-template-columns:48px 1fr;font-size:12px;line-height:18px;row-gap:2px}
.connect dt{color:var(--white);font-weight:600}
.connect dd{color:#bbb}
.parent-mark{position:absolute;left:907px;top:2050px;width:166px;text-align:center;font-family:"Open Sans",sans-serif;font-weight:400;color:#8a8a8a}
.parent-mark .name{font-size:27px;letter-spacing:2px;line-height:1}
.parent-mark .kind{font-size:11px;letter-spacing:4px;margin-top:4px}
.bottom-bar{position:absolute;left:0;top:2163px;width:1200px;height:59px;background:var(--footer-deep);font-size:12px;color:#cfcfcf}
.bottom-bar .copy{position:absolute;left:112px;top:21px}
.bottom-bar .legal{position:absolute;right:109px;top:21px}
</style>
</head>
<body>

<header class="site-header">
  <div class="brand">
    <div class="brand-dot"></div>
    <div class="brand-name"><span class="main">TALVERA</span><span class="sub">TECHNICAL SERVICES</span></div>
  </div>
  <nav class="nav">
    <a class="home" href="#">
      <svg width="16" height="14" viewBox="0 0 16 14"><path d="M8 0 0 7h2v7h4V9h4v5h4V7h2z" fill="#fff"/></svg>Home
    </a>
    <a href="#" style="left:683px">information</a>
    <a href="#" style="left:813px">Services</a>
    <a href="#" style="left:920px">Clients</a>
    <a href="#" style="left:1021px">Contact Us</a>
  </nav>
</header>

<section class="hero" role="img" aria-label="Photo of a business team meeting around a conference table">
  <div class="hero-title light" style="top:228px">IRREVOCABLY</div>
  <div class="hero-title bold" style="top:284px">COMMITTED TO YOUR SUCCESS</div>
  <svg class="divider" style="left:190px;top:362px" width="823" height="14"><line x1="0" y1="7" x2="823" y2="7" stroke="#fff" stroke-width="1.5"/><circle cx="411.5" cy="7" r="5.5" fill="#fff"/></svg>
</section>

<section class="about">
  <h2 class="section-title" style="top:760px">ABOUT US</h2>
  <svg class="divider" style="left:505px;top:808px" width="190" height="14"><line x1="0" y1="7" x2="80" y2="7" stroke="#111"/><line x1="110" y1="7" x2="190" y2="7" stroke="#111"/><circle cx="95" cy="7" r="5" fill="#111"/></svg>
  <p class="about-text">Lorem ipsum dolor sit amet, consectetur adipiscing elit, sed do eiusmod tempor incididunt ut labore et dolore magna aliqua. Ut enim ad minim veniam, quis nostrud exercitation ullamco laboris nisi ut aliquip ex ea commodo consequat duis aute irure dolor in reprehenderit in voluptate velit esse cillum dolore eu fugiat nulla pariatur. Excepteur sint occaecat cupidatat non proident.</p>
</section>

<section class="services">
  <h2 class="section-title" style="top:58px;color:#fff">OUR SERVICES</h2>
  <svg class="divider" style="left:478px;top:111px" width="244" height="14"><line x1="0" y1="7" x2="104" y2="7" stroke="#fff"/><line x1="140" y1="7" x2="244" y2="7" stroke="#fff"/><circle cx="122" cy="7" r="5" fill="#fff"/></svg>

  <div class="service" style="left:86px">
    <div class="disc"><svg width="60" height="52" viewBox="0 0 60 52"><rect x="22" y="0" width="16" height="13" fill="#111"/><path d="M30 13v10M8 23h44M8 23v8M30 23v8M52 23v8" stroke="#111" stroke-width="3" fill="none"/><rect x="0" y="31" width="16" height="13" fill="#111"/><rect x="22" y="31" width="16" height="13" fill="#111"/><rect x="44" y="31" width="16" height="13" fill="#111"/></svg></div>
    <div class="label">NETWORKING</div>
  </div>
  <div class="service" style="left:284px">
    <div class="disc"><svg width="58" height="58" viewBox="0 0 58 58"><g fill="#111"><circle cx="29" cy="29" r="18"/><rect x="25" y="2" width="8" height="12"/><rect x="25" y="44" width="8" height="12"/><rect x="2" y="25" width="12" height="8"/><rect x="44" y="25" width="12" height="8"/><rect x="25" y="2" width="8" height="12" transform="rotate(45 29 29)"/><rect x="25" y="2" width="8" height="12" transform="rotate(-45 29 29)"/><rect x="25" y="44" width="8" height="12" transform="rotate(45 29 29)"/><rect x="25" y="44" width="8" height="12" transform="rotate(-45 29 29)"/></g><circle cx="29" cy="29" r="7" fill="#fff"/></svg></div>
    <div class="label">ACCESS CONTROL</div>
  </div>
  <div class="service" style="left:490px">
    <div class="disc"><svg width="60" height="60" viewBox="0 0 60 60"><g fill="#111"><circle cx="30" cy="18" r="11"/><rect x="27" y="2" width="6" height="6"/><rect x="27" y="28" width="6" height="6"/><rect x="14" y="15" width="6" height="6"/><rect x="40" y="15" width="6" height="6"/><path d="M6 60c0-14 10-22 24-22s24 8 24 22z"/></g><circle cx="30" cy="18" r="4" fill="#fff"/></svg></div>
    <div class="label">AUTOMATION</div>
  </div>
  <div class="service" style="left:687px">
    <div class="disc"><svg width="60" height="54" viewBox="0 0 60 54"><g fill="#111"><rect x="4" y="38" width="9" height="16"/><rect x="17" y="30" width="9" height="24"/><rect x="30" y="22" width="9" height="32"/><rect x="43" y="14" width="9" height="40"/><path d="M4 30 34 6l-4-4h14v14l-4-4L8 34z"/></g></svg></div>
    <div class="label">PROJECT MANAGEMENT</div>
  </div>
  <div class="service" style="left:897px">
    <div class="disc"><svg width="52" height="60" viewBox="0 0 52 60"><g fill="#111"><path d="M6 14 30 4v56H6z"/><rect x="32" y="14" width="14" height="46"/><rect x="0" y="56" width="52" height="4"/></g><g fill="#fff"><rect x="11" y="20" width="4" height="32"/><rect x="20" y="16" width="4" height="36"/><rect x="36" y="20" width="3" height="34"/></g></svg></div>
    <div class="label">SERVICE STAFFING</div>
  </div>
</section>

<section class="clients">
  <h2 class="section-title" style="top:1469px">OUR CLIENTS</h2>
  <svg class="divider" style="left:487px;top:1516px" width="226" height="14"><line x1="0" y1="7" x2="96" y2="7" stroke="#111"/><line x1="130" y1="7" x2="226" y2="7" stroke="#111"/><circle cx="113" cy="7" r="5" fill="#111"/></svg>
  <svg class="arrow" style="left:90px" width="16" height="28" viewBox="0 0 16 28"><path d="M14 2 3 14l11 12" stroke="#ddd" stroke-width="4" fill="none"/></svg>
  <div class="client-row">
    <div class="client">Fizzmont</div>
    <div class="client is-active">Grainholt</div>
    <div class="client">Starbrook</div>
  </div>
  <svg class="arrow" style="left:1097px" width="16" height="28" viewBox="0 0 16 28"><path d="M2 2l11 12L2 26" stroke="#ddd" stroke-width="4" fill="none"/></svg>
</section>

<footer class="site-footer-wrap">
  <div class="site-footer"></div>
  <h3 class="footer-heading" style="left:110px;top:1886px">UPCOMING EVENTS</h3>
  <div class="event" style="top:1922px"><div class="date"><b>22</b><span>JAN</span></div><p>Lorem ipsum dolor sit amet, con-sectetur adipiscing elit. Cras imper-diet quis turpis aliquet mollis.</p></div>
  <div class="event" style="top:1995px"><div class="date"><b>22</b><span>JAN</span></div><p>Lorem ipsum dolor sit amet, con-sectetur adipiscing elit. Cras imper-diet quis turpis aliquet mollis.</p></div>
  <div class="event" style="top:2068px"><div class="date"><b>22</b><span>JAN</span></div><p>Lorem ipsum dolor sit amet, con-sectetur adipiscing elit. Cras imper-diet quis turpis aliquet mollis.</p></div>

  <h3 class="footer-heading" style="left:437px;top:1886px">LATEST NEWS</h3>
  <div class="news" style="top:1922px"><p>Lorem ipsum dolor sit amet, con-sectetur adipiscing elit.</p><small>Sat ; Jan 22,2015</small></div>
  <div class="news" style="top:1993px"><p>Lorem ipsum dolor sit amet, con-sectetur adipiscing elit.</p><small>Sat ; Jan 22,2015</small></div>
  <div class="news" style="top:2064px"><p>Lorem ipsum dolor sit amet, con-sectetur adipiscing elit.</p><small>Sat ; Jan 22,2015</small></div>

  <h3 class="footer-heading" style="left:720px;top:1886px">QUICK LINKS</h3>
  <ul class="quick-links"><li>Home</li><li>Infromation</li><li>Services</li><li>Contact</li></ul>

  <h3 class="footer-heading" style="left:718px;top:2029px">SOCIALIZE WITH US</h3>
  <div class="social"><span><i></i>Loopa</span><span><i></i>Gridly</span><span><i></i>Pipit</span></div>

  <h3 class="footer-heading" style="left:907px;top:1884px">CONNECT WITH US</h3>
  <div class="connect">
    <p>Lorem Ipsum is simply dummy text of the printing.</p>
    <dl><dt>Call</dt><dd>: 555-014-2290</dd><dt>Email</dt><dd>: info@talveramail.com</dd></dl>
  </div>
  <div class="parent-mark" style="top:2062px"><div class="name">DRESGAN</div><div class="kind">ENTERPRISES</div></div>

  <div class="bottom-bar">
    <span class="copy">Copyrights © 2015. Talvera Technical Services . All Rights Reserved</span>
    <span class="legal">Privacy Policy &nbsp; | &nbsp; Terms &amp; Condition</span>
  </div>
</footer>

</body>
</html>
```